依頼詳細
すでに手元にある名刺を見ていただけますか?

これを新たなデザインで刷新します。
必要なイラストや画像などはある程度ご用意できます。

何かこう見たときに「おぉ」となるようなデザインに変更できませんかね(´;ω;`)

奇抜なもの、スタイリッシュなもの、(この人はこんな感じなのだと)認識されやすいもののイメージです。

よろしくお願いします!
記載項目
森川塾:森川 晴人
電号:09058274316
メール:mrkw218@rakuhomail.jp

(裏面は特に希望無しです)
希望イメージ
シンプル 複雑
単色 カラフル
暗い 明るい
日常 高級
遊び心 厳粛
未来的 伝統的
女性的 男性的
希望する色
赤系、黄・オレンジ系、緑系、赤好み、虎は黄・黒、ネクタイは緑。ですが色に指定ありません。
納品ファイル
• PNG形式 (.png)
補足説明
ご不明な点がございましたらお気軽にメッセージください。
なにとぞよろしくお願いしますm(__)m
たくさんのご応募ありがとうございます!当選者が決まりました。

気に入った作品が多数あります。しかし予算上、満額は厳しいですが購入を考えています。

星マークの入った方にお声がけしていきますが、ご希望される方はその可否や条件をお知らせいただけるとスムーズです。

どうぞよろしくお願いします。
■ 選んだ理由

新しく描き起こしていただいた似顔絵はとても似ており、知り合いからも高評価です。
気に入ったので、修正依頼から即座に対応してもらえました。
誠にありがとうございます。

■ 提案者全員のお礼・コメント

ご提案いただきまして、誠にありがとうございました。
とても良いデザインがたくさん集まりました。
別途お声がけできればと考えています。

```html
<!DOCTYPE html>
<html lang="ja">
<head>
<meta charset="utf-8">
<title>森川塾 名刺</title>
<link href="https://fonts.googleapis.com/css2?family=Noto+Sans+JP:wght@500;700;900&display=swap" rel="stylesheet">
<style>
  :root {
    --ink: #000000;
    --paper: #ffffff;
    --accent: #fff100;
    --mascot-light: #e8e8e8;
    --mascot-dark: #2a2a2a;
  }
  html, body {
    margin: 0;
    padding: 0;
    width: 726px;
    height: 1200px;
    overflow: hidden;
    background: var(--ink);
  }
  .card {
    position: relative;
    width: 726px;
    height: 1200px;
    background: var(--ink);
    font-family: "Noto Sans JP", sans-serif;
    color: var(--paper);
    overflow: hidden;
  }
  .school-char {
    position: absolute;
    font-weight: 900;
    font-size: 390px;
    line-height: 1;
    width: 370px;
    text-align: center;
    letter-spacing: 0;
  }
  .school-char--first { left: 4px; top: 0; color: var(--accent); }
  .school-char--second { left: 356px; top: 0; color: var(--paper); }
  .school-char--third { left: 356px; top: 392px; color: var(--paper); }
  .mascot {
    position: absolute;
    left: 48px;
    top: 430px;
    width: 292px;
    height: 320px;
    display: block;
  }
  .name-band {
    position: absolute;
    left: 0;
    top: 778px;
    width: 726px;
    height: 122px;
    background: var(--accent);
  }
  .name-band__name {
    position: absolute;
    left: 36px;
    top: 10px;
    margin: 0;
    font-weight: 500;
    font-size: 84px;
    line-height: 1.2;
    color: var(--ink);
    letter-spacing: 2px;
  }
  .name-romaji {
    position: absolute;
    left: 36px;
    top: 900px;
    margin: 0;
    font-weight: 700;
    font-size: 28px;
    line-height: 1.4;
    letter-spacing: 1px;
  }
  .contact {
    position: absolute;
    left: 36px;
    top: 945px;
    margin: 0;
  }
  .contact__label {
    font-weight: 500;
    font-size: 28px;
    line-height: 1.5;
    margin: 0;
  }
  .contact__value {
    font-weight: 700;
    font-size: 30px;
    line-height: 1.4;
    margin: 0 0 2px;
    letter-spacing: 1px;
  }
</style>
</head>
<body>
  <main class="card">
    <div class="school-char school-char--first">森</div>
    <div class="school-char school-char--second">川</div>
    <div class="school-char school-char--third">塾</div>

    <svg class="mascot" role="img" aria-label="黒と白で描かれた虎の顔のイラスト" viewBox="0 0 292 320">
      <defs>
        <radialGradient id="mascot-fill" cx="50%" cy="50%" r="55%">
          <stop offset="0%" stop-color="var(--mascot-light)"/>
          <stop offset="100%" stop-color="var(--mascot-dark)"/>
        </radialGradient>
      </defs>
      <rect x="0" y="0" width="292" height="320" rx="120" fill="url(#mascot-fill)"/>
    </svg>

    <div class="name-band">
      <h1 class="name-band__name">森川晴人</h1>
    </div>
    <p class="name-romaji">Morikawa Haruto</p>

    <div class="contact">
      <p class="contact__label">電話番号</p>
      <p class="contact__value">090-5827-4316</p>
      <p class="contact__label">メールアドレス</p>
      <p class="contact__value">mrkw218@rakuhomail.jp</p>
    </div>
  </main>
</body>
</html>
```